Need business cards for our e-assessment business

We need professional looking business cards for our e-assessment business based in Europe. Our company is called Velmora.

You can just use sample name and addresses.

The colours we use are:

#70abe4 (blue)
#FF6600 (orange)

The back side should say: Online testing made simple

This is the print-shop we are using. Please look at the link for info about formats: http://nl.pribbly-print.com/help/faq/using-my-own-artwork.html

Target Market(s)

Target market is education and large corporations

Industry/Entity Type

Business

```html
<!DOCTYPE html>
<html lang="en">
<head>
<meta charset="utf-8">
<title>Velmora business cards</title>
<link rel="stylesheet" href="https://fonts.googleapis.com/css2?family=Quicksand:wght@400;500;600&display=swap">
<style>
  :root {
    --orange: #f26522;
    --blue: #70abe4;
    --ink: #2b2b2b;
    --paper: #ffffff;
    --paper-grey: #d9d9d9;
    --stage: #ecebe8;
  }
  * { margin: 0; padding: 0; box-sizing: border-box; }
  html, body { width: 1200px; height: 871px; overflow: hidden; }
  body {
    background: var(--stage);
    font-family: "Quicksand", "Century Gothic", sans-serif;
    position: relative;
  }
  .card {
    position: absolute;
    width: 520px;
    height: 325px;
    top: 273px;
    overflow: hidden;
    box-shadow: 0 6px 18px rgba(0,0,0,0.18);
  }
  /* back side */
  .card-back {
    left: 50px;
    background: linear-gradient(135deg, var(--paper) 0%, #f1f1f1 45%, var(--paper-grey) 100%);
  }
  .back-mark {
    position: absolute;
    width: 150px; height: 150px;
    left: 185px; top: 50px;
    border-radius: 50%;
    background: var(--orange);
  }
  .tagline {
    position: absolute;
    left: 0; right: 0; top: 228px;
    text-align: center;
    color: var(--blue);
    font-size: 17px;
    font-weight: 500;
    letter-spacing: 1.5px;
  }
  /* front side */
  .card-front {
    left: 630px;
    background: var(--paper);
  }
  .brand {
    position: absolute;
    top: 42px; left: 0; right: 0;
    display: flex; align-items: center; justify-content: center;
    gap: 16px;
  }
  .brand-dot {
    width: 58px; height: 58px;
    border-radius: 50%;
    background: var(--orange);
  }
  .brand-name {
    font-size: 54px;
    font-weight: 500;
    color: var(--ink);
    letter-spacing: 1px;
    line-height: 1;
  }
  .band-name {
    position: absolute;
    left: 0; top: 150px;
    width: 290px; height: 108px;
    background: var(--orange);
    color: var(--paper);
    font-size: 19px;
    font-weight: 500;
    letter-spacing: 1.5px;
    padding: 22px 0 0 36px;
  }
  .band-contact {
    position: absolute;
    left: 290px; top: 180px;
    width: 230px; height: 108px;
    background: var(--blue);
    color: var(--paper);
    font-size: 11px;
    font-weight: 500;
    font-style: normal;
    letter-spacing: 1px;
    line-height: 1.6;
    text-align: center;
    padding-top: 26px;
  }
  .company { color: var(--orange); font-weight: 600; }
</style>
</head>
<body>
  <section class="card card-back" aria-label="Card back">
    <div class="back-mark"></div>
    <p class="tagline">Online testing made simple</p>
  </section>

  <section class="card card-front" aria-label="Card front">
    <div class="brand">
      <div class="brand-dot"></div>
      <span class="brand-name">velmora</span>
    </div>
    <div class="band-name">Mara L Voss</div>
    <address class="band-contact">
      <span class="company">velmora inc</span><br>
      18 Keller Lane, Ashbridge<br>
      QLD 4092
    </address>
  </section>
</body>
</html>
```